Business Card Design for venture capital-focused company

I have a logo (attached), and would like business cards designed using the attached logo. Audience is mainly financial executives; services included finance/ accounting/ dashboards/ etc. Open to different design ideas. Thanks for your consideration.

Target Market(s)

Financial Executives, Venture Capital, etc.

Industry/Entity Type

Venture Capital

Contact Information for Business Card

Vantry Ledger Metrics LLC
418 N Calloway Street
Arlington Heights, IL 60017

Font styles to use
Serif
Sans Serif

```html
<!DOCTYPE html>
<html lang="en">
<head>
<meta charset="utf-8">
<title>Vantry Ledger Metrics — Business Cards</title>
<link rel="stylesheet" href="https://fonts.googleapis.com/css2?family=Open+Sans:wght@400;600;700&display=swap">
<style>
  :root {
    --brand-blue: #1f5fd0;
    --brand-blue-light: #2f74e0;
    --steel-grey: #bfc2c6;
    --steel-grey-light: #e4e6e8;
    --ink-grey: #6f7276;
    --paper: #ffffff;
    --backdrop: #e9ebee;
  }
  * { margin: 0; padding: 0; box-sizing: border-box; }
  html, body {
    width: 1200px; height: 900px; overflow: hidden;
    background: var(--backdrop);
    font-family: "Open Sans", Arial, sans-serif;
  }
  .canvas { position: relative; width: 1200px; height: 900px; }

  .card {
    position: absolute;
    background: var(--paper);
    border-radius: 22px;
    overflow: hidden;
    box-shadow: 0 10px 30px rgba(20, 30, 50, 0.18);
  }

  /* ---------- Back card (vertical, contact side) ---------- */
  .card-contact { left: 130px; top: 170px; width: 320px; height: 560px; }
  .card-contact .bands { position: absolute; inset: 0; }
  .card-contact .wordmark {
    position: absolute; left: 0; top: 120px; width: 100%;
    display: flex; align-items: center; justify-content: center; gap: 10px;
    color: var(--paper);
  }
  .wordmark .dot {
    width: 12px; height: 12px; border-radius: 50%;
    background: currentColor; flex: none;
  }
  .wordmark .name {
    font-weight: 600; font-size: 22px; letter-spacing: 0.5px; line-height: 1.15;
    text-align: center;
  }
  .details { position: absolute; left: 36px; top: 330px; right: 24px; }
  .person-name { color: var(--brand-blue); font-weight: 700; font-size: 22px; line-height: 1.2; }
  .person-role { color: var(--ink-grey); font-size: 15px; margin-bottom: 16px; }
  .address { color: var(--brand-blue); font-weight: 700; font-size: 15px; line-height: 1.35; margin-bottom: 10px; }
  .contact-row {
    display: flex; align-items: center; gap: 9px;
    color: var(--ink-grey); font-size: 14px; line-height: 1.75;
  }
  .contact-row svg { width: 16px; height: 16px; flex: none; }

  /* ---------- Front card (horizontal, brand side) ---------- */
  .card-brand { left: 520px; top: 290px; width: 560px; height: 320px; }
  .card-brand .bands { position: absolute; inset: 0; }
  .card-brand .wordmark {
    position: absolute; left: 0; top: 92px; width: 100%;
    display: flex; align-items: center; justify-content: center; gap: 14px;
    color: var(--brand-blue);
  }
  .card-brand .wordmark .name { font-size: 34px; }
  .card-brand .wordmark .dot { width: 16px; height: 16px; }
  .website {
    position: absolute; left: 0; bottom: 24px; width: 100%;
    text-align: center; color: var(--paper); font-weight: 700; font-size: 15px; letter-spacing: 0.3px;
  }
</style>
</head>
<body>
<main class="canvas">

  <section class="card card-contact" aria-label="Business card, contact side">
    <svg class="bands" viewBox="0 0 320 560" aria-hidden="true">
      <defs>
        <linearGradient id="blueFill" x1="0" y1="0" x2="1" y2="1">
          <stop offset="0" stop-color="#1b56c6"/>
          <stop offset="1" stop-color="#2f74e0"/>
        </linearGradient>
        <linearGradient id="greyFill" x1="0" y1="0" x2="1" y2="0">
          <stop offset="0" stop-color="#e4e6e8"/>
          <stop offset="1" stop-color="#b9bcc0"/>
        </linearGradient>
      </defs>
      <polygon points="0,0 320,0 320,250 0,318" fill="url(#greyFill)"/>
      <polygon points="0,0 320,0 320,232 0,300" fill="url(#blueFill)"/>
    </svg>
    <div class="wordmark">
      <span class="dot"></span>
      <span class="name">Vantry Ledger<br>Metrics</span>
    </div>
    <div class="details">
      <p class="person-name">Example Name</p>
      <p class="person-role">Designation</p>
      <p class="address">418 N Calloway Street<br>Arlington Heights, IL 60017</p>
      <p class="contact-row">
        <svg viewBox="0 0 16 16" aria-hidden="true"><rect width="16" height="16" rx="2" fill="#1f5fd0"/><path d="M5 3.5l2 2-1 1.3c.7 1.4 1.8 2.5 3.2 3.2l1.3-1 2 2-1.2 1.5C8 12.5 3.5 8 3.5 4.7z" fill="#fff"/></svg>
        (000) 000 0880
      </p>
      <p class="contact-row">
        <svg viewBox="0 0 16 16" aria-hidden="true"><rect width="16" height="16" rx="2" fill="#1f5fd0"/><rect x="5" y="2.5" width="6" height="11" rx="1.2" fill="#fff"/><rect x="6.2" y="4" width="3.6" height="6.5" fill="#1f5fd0"/></svg>
        (000) 000 0005
      </p>
      <p class="contact-row">
        <svg viewBox="0 0 16 16" aria-hidden="true"><rect width="16" height="16" rx="2" fill="#1f5fd0"/><rect x="3" y="4.5" width="10" height="7" fill="#fff"/><path d="M3 4.5l5 4 5-4" fill="none" stroke="#1f5fd0" stroke-width="1.1"/></svg>
        info@vantryledgermetrics.com
      </p>
    </div>
  </section>

  <section class="card card-brand" aria-label="Business card, brand side">
    <svg class="bands" viewBox="0 0 560 320" aria-hidden="true">
      <polygon points="0,218 560,250 560,320 0,320" fill="#c9ccd0"/>
      <polygon points="0,236 560,266 560,320 0,320" fill="#1f5fd0"/>
    </svg>
    <div class="wordmark">
      <span class="dot"></span>
      <span class="name">Vantry Ledger Metrics</span>
    </div>
    <p class="website">www.vantryledgermetrics.com</p>
  </section>

</main>
</body>
</html>
```